VQB 2023 Postcard

We need a postcard created for an upcoming trade show. We had something made for our sister company a while back and are interested in a similar look. We have included images and some layouts that can be used along with our logo. We like earthy colors, gray and black are okay too. We would like it to be 5x7 and landscape orientation. We have attached the wording we would like to see on the back of the card with changes made in red.
Target Market(s)
retailers
Industry/Entity Type
wedding ring
Colors
Designer to choose only greyscale colors for use in the design.

```html
<!DOCTYPE html>
<html lang="en">
<head>
<meta charset="utf-8">
<title>Halden Rings – Trade Show Postcard</title>
<link href="https://fonts.googleapis.com/css2?family=Open+Sans:ital,wght@0,400;0,600;0,800;1,400&display=swap" rel="stylesheet">
<style>
  :root {
    --backdrop: #6d6e71;
    --card-front: #2f2f31;
    --front-mark: #e6e6e6;
    --front-text: #f0f0f0;
    --ink: #111111;
    --paper: #ffffff;
    --bar-start: #8a8b8d;
    --bar-end: #ffffff;
    --footer: #0d0d0d;
    --metal-light: #f1f1f1;
    --metal-mid: #cfcfcf;
    --metal-warm: #ddc8a6;
  }
  * { box-sizing: border-box; margin: 0; padding: 0; }
  html, body {
    width: 1200px; height: 1200px; overflow: hidden;
    background: var(--backdrop);
    font-family: "Open Sans", sans-serif;
    color: var(--ink);
  }
  .canvas { position: relative; width: 1200px; height: 1200px; }

  /* Front of card */
  .card-front {
    position: absolute; left: 268px; top: 49px;
    width: 666px; height: 476px;
    background: var(--card-front);
  }
  .front-brand {
    position: absolute; left: 0; right: 0; top: 140px;
    display: flex; flex-direction: column; align-items: center;
  }
  .front-brand .brand-square {
    width: 164px; height: 164px; background: var(--front-mark);
  }
  .front-name {
    margin-top: 16px;
    font-size: 34px; font-weight: 400; letter-spacing: 4px;
    color: var(--front-text); text-transform: uppercase;
  }

  /* Back of card */
  .card-back {
    position: absolute; left: 265px; top: 619px;
    width: 669px; height: 481px;
    background: var(--paper);
  }
  .back-brand {
    position: absolute; left: 0; right: 0; top: 26px;
    display: flex; justify-content: center; align-items: center; gap: 12px;
  }
  .back-brand .brand-square { width: 54px; height: 54px; background: var(--ink); }
  .back-name {
    font-size: 38px; font-weight: 400; letter-spacing: 3px;
    text-transform: uppercase; color: var(--ink);
  }
  .section-bar {
    position: absolute; left: 28px; width: 416px; height: 33px;
    background: linear-gradient(90deg, var(--bar-start) 0%, #d4d4d5 45%, var(--bar-end) 100%);
    display: flex; align-items: center; padding-left: 16px;
    font-size: 20px; font-weight: 800; letter-spacing: 1.2px;
    white-space: nowrap;
  }
  .bar-programs { top: 117px; }
  .bar-source { top: 289px; }
  .feature-list {
    position: absolute; left: 28px; top: 168px; list-style: none;
    font-size: 11px; line-height: 18px;
  }
  .feature-list li { display: flex; align-items: center; gap: 10px; }
  .feature-list li::before {
    content: ""; width: 9px; height: 9px; border-radius: 50%;
    border: 1.2px solid var(--ink); flex: none;
  }
  .call-line {
    position: absolute; left: 28px; top: 327px;
    font-size: 12px; font-style: italic;
  }
  .perks {
    position: absolute; left: 28px; top: 350px;
    display: grid; grid-template-columns: 212px 200px;
    font-size: 11.5px; font-weight: 600; line-height: 19.5px;
    text-transform: uppercase;
  }
  .ring-photos {
    position: absolute; left: 466px; top: 96px; width: 160px; height: 318px;
    background: radial-gradient(ellipse at 65% 12%, var(--metal-warm) 0%, transparent 28%),
                linear-gradient(180deg, var(--metal-light), var(--metal-mid) 55%, var(--metal-light));
    border-radius: 8px;
  }
  .footer-band {
    position: absolute; left: 0; right: 0; bottom: 0; height: 38px;
    background: var(--footer); color: var(--paper);
    display: flex; align-items: center; justify-content: center;
    font-size: 9px; white-space: nowrap;
  }
</style>
</head>
<body>
<div class="canvas">

  <section class="card-front">
    <div class="front-brand">
      <div class="brand-square"></div>
      <div class="front-name">Halden Rings</div>
    </div>
  </section>

  <section class="card-back">
    <div class="back-brand">
      <div class="brand-square"></div>
      <div class="back-name">Halden Rings</div>
    </div>

    <h2 class="section-bar bar-programs">PREMIUM CUSTOMIZED PROGRAMS</h2>
    <ul class="feature-list">
      <li>Promote your own brand, rings stamped with your specified logo.</li>
      <li>Offer rings in any width, 3 thicknesses and all precious metals</li>
      <li>Combine &amp; customize 5500 ring designs.</li>
      <li>Sell in Platinum, 18kt, 14kt &amp; 10 kt</li>
      <li>Sample kits starting as low as $900</li>
      <li>Program Performance Money Back Guarantee</li>
    </ul>

    <h2 class="section-bar bar-source">YOUR TRUSTED SOURCE FOR RINGS</h2>
    <p class="call-line">Call 800-555-0147 for more information</p>
    <div class="perks">
      <span>Easy Pricing System</span><span>Free Shipping</span>
      <span>Scrap Buyout Options</span><span>Pre-Tagged Samples</span>
      <span>1 Week Turnaround</span><span>Competitive Pricing</span>
      <span>Family Owned and Operated</span><span>Made Proudly in the USA</span>
    </div>

    <div class="ring-photos" role="img" aria-label="Product photos of five wedding bands in yellow gold, rose gold, brushed white gold, diamond channel-set and two-tone finishes"></div>

    <footer class="footer-band">
      412 Orchard Lane, Millbrook NY&nbsp; 12545 | p: 555.014.2290, 800-555-0147 | E: sales@haldenrings.com | www.haldenrings.com | social/HaldenRings
    </footer>
  </section>

</div>
</body>
</html>
```